PostPeddle Social Sharing Platform Needs a Redesign (2 pages / Design only)

PostPeddle is a popular social sharing platform for bloggers and marketers. The site has been quite popular for a few years now, but the site's design is looking quite dated. We're looking for a brand new design to give the service a facelift.

We are looking for a modern and fresh design that keeps all the existing functionality intact. Would prefer designs that incorporate the color blue in them.

We would like the two attached screenshots to be redesigned and submitted - using he same content. Please do not submit a redesign of the front page (non-logged in version). Redesign the 2 attached pages only, and the final deliverable is these two pages as layered PSD files.

Target Market(s)

bloggers, internet marketers

Industry/Entity Type

Social

Number of Pages Required

2 page

Requirements
Must have
• All existing functionality must be intact as seen from the screenshots.
Should not have
• Please do not submit designs based on existing front page (non-logged in version). Use attached screenshots (file 1 and 2) as a guide of existing functionality.

```html
<!DOCTYPE html>
<html lang="en">
<head>
<meta charset="utf-8">
<title>PostPeddle – Dashboard</title>
<link href="https://fonts.googleapis.com/css2?family=Open+Sans:wght@400;600;700&display=swap" rel="stylesheet">
<style>
:root{
  --blue:#1a6bb5;
  --blue-dark:#145a9c;
  --ink:#333;
  --muted:#777;
  --nav:#2a2a2a;
  --page:#ececec;
  --card:#fff;
  --item:#f0f0f0;
  --line:#dcdcdc;
  --footer-dark:#2b2b2b;
}
*{box-sizing:border-box;margin:0;padding:0}
html,body{width:709px;height:1200px;overflow:hidden}
body{position:relative;background:var(--page);font-family:"Open Sans",Arial,sans-serif;color:var(--ink);font-size:8px}
.hero{position:absolute;left:0;top:0;width:709px;height:244px;background:linear-gradient(180deg,#6c7a8c 0%,#8e8a86 45%,#a79b90 100%)}
.topbar{position:absolute;left:42px;top:24px;width:624px;height:145px;background:rgba(240,240,240,.95)}
.brand{position:absolute;left:16px;top:22px;display:flex;align-items:center;gap:6px;font-size:20px;font-weight:700;color:#17406e;letter-spacing:-.3px}
.brand .mark{width:12px;height:12px;background:var(--blue)}
.user{position:absolute;right:22px;top:17px;width:124px;height:29px;border:1px solid #bbb;background:#f7f7f7;display:flex;align-items:center;padding:2px}
.user .avatar{width:24px;height:24px;background:linear-gradient(#9aa3ad,#5e646b)}
.user span{margin-left:14px;font-size:10px;color:#222;flex:1}
.user svg{margin-right:10px}
.nav{position:absolute;left:0;top:62px;width:624px;height:29px;background:var(--nav);display:flex}
.nav a{color:#fff;font-size:8.2px;font-weight:600;text-decoration:none;line-height:29px;padding:0 12.5px;white-space:nowrap}
.nav a.active{background:var(--blue);padding:0 12px;margin-right:4px}
.filters{position:absolute;left:0;top:91px;width:624px;height:54px}
.filters .prompt{position:absolute;left:12px;top:7px;color:var(--blue);font-size:10px;font-weight:600}
.filters label{position:absolute;top:28px;font-style:italic;font-size:8.5px;font-weight:600;color:#444}
.select{position:absolute;top:26px;height:17px;background:#fff;border:1px solid #bbb;font-size:7.5px;color:#444;line-height:15px;padding-left:6px}
.select::after{content:"";position:absolute;right:0;top:-1px;width:17px;height:17px;background:var(--blue)}
.select svg{position:absolute;right:4px;top:5px;z-index:1}
.contest{position:absolute;left:42px;top:186px;color:#fff;font-size:13.5px;font-weight:600}
.btn{position:absolute;left:44px;top:214px;width:79px;height:19px;background:var(--blue);color:#fff;font-size:8.5px;font-weight:600;text-align:center;line-height:19px}
.card{position:absolute;background:var(--card);border:1px solid var(--line)}
.intro{left:42px;top:263px;width:413px;height:122px}
.intro .art{position:absolute;left:8px;top:8px;width:150px;height:104px;background:radial-gradient(circle at 45% 60%,#2c6fc4,#9ec6ee 60%,#fff 80%)}
.intro h2{position:absolute;left:171px;top:12px;color:var(--blue);font-size:12px;font-weight:600;line-height:16px}
.intro p{position:absolute;left:171px;top:51px;width:222px;color:var(--muted);font-size:8.4px;line-height:15px}
.credits{position:absolute;left:490px;top:263px;width:176px;height:87px;background:var(--blue);color:#fff;text-align:center}
.credits .art{position:absolute;left:-14px;top:12px;width:70px;height:70px;background:radial-gradient(circle at 50% 60%,#2f6dbd,#7fb0e6 70%);border-radius:50%}
.credits .num{position:absolute;left:70px;width:106px;top:3px;font-size:23px;font-weight:600}
.credits .lbl{position:absolute;left:70px;width:106px;top:37px;font-size:9px}
.credits .cta{position:absolute;left:70px;width:106px;top:56px;font-size:8.5px;font-weight:700;line-height:12px}
.feed{left:42px;top:405px;width:413px;height:705px}
.card h3{color:var(--blue);font-size:12.5px;font-weight:600;position:absolute;left:13px;top:9px}
.tweet{position:absolute;left:6px;width:400px;height:69px;background:var(--item)}
.tweet .pic{position:absolute;left:6px;top:6px;width:62px;height:56px;background:linear-gradient(135deg,#cfd3d8,#7f858c)}
.tweet .handle{position:absolute;left:74px;top:6px;color:var(--blue);font-size:9.5px;font-weight:600}
.tweet p{position:absolute;left:74px;top:24px;width:320px;font-size:7.7px;line-height:12.5px;color:#555}
.tweet p a{color:var(--blue);font-weight:600;text-decoration:none}
.who{left:474px;top:380px;width:192px;height:422px}
.grid{position:absolute;left:6px;top:32px;display:grid;grid-template-columns:repeat(4,43px);gap:2px 2px}
.grid div{height:43px;background:linear-gradient(160deg,#d8dde2,#6d7379)}
.who h4{position:absolute;left:11px;top:221px;color:var(--blue);font-size:11px;font-weight:600}
.tops{position:absolute;left:11px;top:246px;list-style:none}
.tops li{display:flex;align-items:center;height:24px;font-size:8.5px;color:#444}
.tops .av{width:21px;height:19px;background:linear-gradient(#c9cdd2,#6a7077);margin-right:8px}
.tops b{color:var(--blue);font-weight:600;margin-right:5px}
.featured{left:474px;top:822px;width:192px;height:284px}
.site{position:absolute;left:6px;width:180px;background:linear-gradient(120deg,#3fb7b0,#8fd6d3 55%,#e9d9c5)}
.site .url{position:absolute;left:0;bottom:0;width:100%;height:27px;background:rgba(30,30,30,.75);color:#4fa9ff;font-size:8px;line-height:27px;padding-left:10px}
.site2{background:linear-gradient(#f3f5f7,#dfe4ea)}
.foot-links{position:absolute;left:0;top:1130px;width:709px;height:35px;background:var(--blue);display:flex;justify-content:center;align-items:center;gap:6px;font-size:8.5px;color:#bcd5ef}
.foot-links a{color:#cfe0f2;text-decoration:none}
.foot-links a.current{color:#fff;font-weight:600}
.copy{position:absolute;left:0;top:1165px;width:709px;height:35px;background:var(--footer-dark);color:#8a8a8a;font-size:8px;text-align:center;line-height:35px}
</style>
</head>
<body>
<div class="hero" role="img" aria-label="Blurred photo of a large crowd"></div>
<header class="topbar">
  <div class="brand"><span class="mark"></span>PostPeddle</div>
  <div class="user"><div class="avatar" role="img" aria-label="User avatar photo"></div><span>Jonaskelby</span>
    <svg width="8" height="5" viewBox="0 0 8 5"><path d="M0 0h8L4 5z" fill="#333"/></svg></div>
  <nav class="nav">
    <a class="active">DASHBOARD</a><a>CHIRPER FOLLOWERS</a><a>SUBMIT TWEET</a><a>ACTIVEITY SUMMARY</a><a>BUY CREDITS</a><a>SETTINGS</a><a>AFFLIATES</a>
  </nav>
  <div class="filters">
    <div class="prompt">Retweet or like To Earn More Credits...</div>
    <label style="left:12px">Order By:</label>
    <div class="select" style="left:53px;width:124px">Most Recent<svg width="8" height="5"><path d="M0 0h8L4 5z" fill="#fff"/></svg></div>
    <div class="select" style="left:182px;width:124px">All Categories<svg width="8" height="5"><path d="M0 0h8L4 5z" fill="#fff"/></svg></div>
    <label style="left:324px">Search:</label>
    <div class="select" style="left:359px;width:254px">Keyword or Chirper handle<svg width="8" height="5"><path d="M0 0h8L4 5z" fill="#fff"/></svg></div>
  </div>
</header>
<div class="contest">See who won our PostPeddle Labor Day Contest</div>
<div class="btn">CLICK HERE</div>

<section class="card intro">
  <div class="art" role="img" aria-label="Illustration of a blue bird mascot with a laptop"></div>
  <h2>PostPeddle - Retweet and<br>Follow Just</h2>
  <p>Since the launch of PostPeddle, many bloggers have seen the benefits of joining the site. Take a look at the testimonials from a few of the prominent bloggers who are using the site to</p>
</section>

<aside class="credits">
  <div class="art" role="img" aria-label="Illustration of the blue bird mascot with a speech bubble"></div>
  <div class="num">315858</div>
  <div class="lbl">Your Credits</div>
  <div class="cta">CLICK HERE TO<br>SUBMIT A RETWEET</div>
</aside>

<section class="card feed">
  <h3>PostPeddle</h3>
  <div class="tweet" style="top:33px"><div class="pic" role="img" aria-label="Member profile photo"></div><div class="handle">@Jonaskelby</div><p>#LOREM IPSUM dolor sit amet, consectetur adipiscing elit. Vestulum pulvinar auctor diam vitae mollis. Morbi at odio rutrum, varius turpisat. <a>http://sollicitin Donec smet</a> vehicula metus. #Vestibulum #accumsan imperdiet massa.</p></div>
  <div class="tweet" style="top:108px"><div class="pic" role="img" aria-label="Member profile photo"></div><div class="handle">@Jonaskelby</div><p>#LOREM IPSUM dolor sit amet, consectetur adipiscing elit. Vestulum pulvinar auctor diam vitae mollis. Morbi at odio rutrum, varius turpisat. <a>http://sollicitin Donec smet</a> vehicula metus. #Vestibulum #accumsan imperdiet massa.</p></div>
  <div class="tweet" style="top:183px"><div class="pic" role="img" aria-label="Member profile photo"></div><div class="handle">@Jonaskelby</div><p>#LOREM IPSUM dolor sit amet, consectetur adipiscing elit. Vestulum pulvinar auctor diam vitae mollis. Morbi at odio rutrum, varius turpisat. <a>http://sollicitin Donec smet</a> vehicula metus. #Vestibulum #accumsan imperdiet massa.</p></div>
  <div class="tweet" style="top:258px"><div class="pic" role="img" aria-label="Member profile photo"></div><div class="handle">@Jonaskelby</div><p>#LOREM IPSUM dolor sit amet, consectetur adipiscing elit. Vestulum pulvinar auctor diam vitae mollis. Morbi at odio rutrum, varius turpisat. <a>http://sollicitin Donec smet</a> vehicula metus. #Vestibulum #accumsan imperdiet massa.</p></div>
  <div class="tweet" style="top:333px"><div class="pic" role="img" aria-label="Member profile photo"></div><div class="handle">@Jonaskelby</div><p>#LOREM IPSUM dolor sit amet, consectetur adipiscing elit. Vestulum pulvinar auctor diam vitae mollis. Morbi at odio rutrum, varius turpisat. <a>http://sollicitin Donec smet</a> vehicula metus. #Vestibulum #accumsan imperdiet massa.</p></div>
  <div class="tweet" style="top:408px"><div class="pic" role="img" aria-label="Member profile photo"></div><div class="handle">@Jonaskelby</div><p>#LOREM IPSUM dolor sit amet, consectetur adipiscing elit. Vestulum pulvinar auctor diam vitae mollis. Morbi at odio rutrum, varius turpisat. <a>http://sollicitin Donec smet</a> vehicula metus. #Vestibulum #accumsan imperdiet massa.</p></div>
  <div class="tweet" style="top:483px"><div class="pic" role="img" aria-label="Member profile photo"></div><div class="handle">@Jonaskelby</div><p>#LOREM IPSUM dolor sit amet, consectetur adipiscing elit. Vestulum pulvinar auctor diam vitae mollis. Morbi at odio rutrum, varius turpisat. <a>http://sollicitin Donec smet</a> vehicula metus. #Vestibulum #accumsan imperdiet massa.</p></div>
  <div class="tweet" style="top:558px"><div class="pic" role="img" aria-label="Member profile photo"></div><div class="handle">@Jonaskelby</div><p>#LOREM IPSUM dolor sit amet, consectetur adipiscing elit. Vestulum pulvinar auctor diam vitae mollis. Morbi at odio rutrum, varius turpisat. <a>http://sollicitin Donec smet</a> vehicula metus. #Vestibulum #accumsan imperdiet massa.</p></div>
  <div class="tweet" style="top:633px"><div class="pic" role="img" aria-label="Member profile photo"></div><div class="handle">@Jonaskelby</div><p>#LOREM IPSUM dolor sit amet, consectetur adipiscing elit. Vestulum pulvinar auctor diam vitae mollis. Morbi at odio rutrum, varius turpisat. <a>http://sollicitin Donec smet</a> vehicula metus. #Vestibulum #accumsan imperdiet massa.</p></div>
</section>

<aside class="card who">
  <h3>Look Who Is Here</h3>
  <div class="grid" role="img" aria-label="Grid of sixteen member profile photos">
    <div></div><div></div><div></div><div></div><div></div><div></div><div></div><div></div>
    <div></div><div></div><div></div><div></div><div></div><div></div><div></div><div></div>
  </div>
  <h4>Top Retweeters:</h4>
  <ul class="tops">
    <li><span class="av" role="img" aria-label="Avatar"></span><b>@Loremispum</b>14343 retweets</li>
    <li><span class="av" role="img" aria-label="Avatar"></span><b>@DigitalKent</b>12354 retweets</li>
    <li><span class="av" role="img" aria-label="Avatar"></span><b>@WriterKeller</b>8670 retweets</li>
    <li><span class="av" role="img" aria-label="Avatar"></span><b>@thedraftsmith</b>8282 retweets</li>
    <li><span class="av" role="img" aria-label="Avatar"></span><b>@follow4followup</b>8265 retweets</li>
    <li><span class="av" role="img" aria-label="Avatar"></span><b>@abelnova</b>7714 retweets</li>
    <li><span class="av" role="img" aria-label="Avatar"></span><b>@DetailReel</b>7139 retweets</li>
  </ul>
</aside>

<aside class="card featured">
  <h3>Featured Websites</h3>
  <div class="site" style="top:33px;height:118px" role="img" aria-label="Screenshot of a featured business website with a woman at the beach"><div class="url">http://freetimeventure.com</div></div>
  <div class="site site2" style="top:160px;height:118px" role="img" aria-label="Screenshot of a featured blog homepage"><div class="url">http://www.carlaameno.com/blog</div></div>
</aside>

<footer>
  <div class="foot-links"><a class="current">Home</a>/<a>About Us</a>/<a>How It Work</a>/<a>Refund Policy</a>/<a>Contact Us</a>/<a>Private Policy</a>/<a>Terms &amp; Conditions</a></div>
  <div class="copy">© Copyright 2014 PostPeddle. All rights reserved.</div>
</footer>
</body>
</html>
```